Harlow Consulting, Business Cards for International Development Consultancy

I'm an independent consultant working in the international development sector. I work with small organisations in developing countries to help them develop their community based programs so that they can be internationally competitive. This means they need to work better with their own communities to deliver meaningful quality work and also improve the accountability of their work so that they can compete for international and domestic funding.

I like the idea of being a connector between community, local organisations and international best practice and back again (ie acknowledging that international best practice can learn a lot from community).

My surname is Harlow - so I'd like the logo to use the idea of web as a connector.

I work with people with sight impairments - would like my card to be useful for low vision (i.e. clear graphics, easy to read font) and no vision (i.e. brail).

Target Market(s)

international non-government organisations (i.e. corvane, lift the villages, brightpath aid), Blue Harbour Green Lantern, government (i.e. Australian Bureau of Overseas Partnerships, consulars), non government agencies,

Industry/Entity Type

Business

Contact Information for Business Card

International Development Consultant
Connecting International Development with Community

Mirela Harlow
Lead Consultant
Phone: +61 412 558127
Email: mharlow.consulting@quillmail.net

Font styles to use
Sans Serif

Colors
eaf1f7
85acd3
d3a5cc
0456a4
a64599
0255a3

Requirements
Nice to have
• brail
Should not have
• fancy fonts - needs to be easy to read.

```html
<!DOCTYPE html>
<html lang="en">
<head>
<meta charset="utf-8">
<title>Harlow Consulting – Business Card</title>
<link rel="stylesheet" href="https://fonts.googleapis.com/css2?family=Oswald:wght@600&family=Raleway:wght@400;500&display=swap">
<style>
  :root {
    --bg: #c4e6dc;
    --card-blue-top: #9ab5dc;
    --card-blue-bottom: #7599cb;
    --band: #ffffff;
    --ink-blue: #0255a3;
    --deep-blue: #0456a4;
    --title-white: #f4f7fb;
    --paper: #ffffff;
    --dots: #2b2b2b;
  }
  * { box-sizing: border-box; margin: 0; padding: 0; }
  html, body { width: 1200px; height: 856px; overflow: hidden; }
  body {
    background: var(--bg);
    display: flex;
    align-items: center;
    justify-content: center;
    gap: 48px;
    font-family: "Raleway", Arial, sans-serif;
  }
  .card {
    width: 540px;
    height: 310px;
    border-radius: 26px;
    position: relative;
    overflow: hidden;
    box-shadow: 0 6px 18px rgba(0,0,0,0.12);
  }
  .card-front {
    background: linear-gradient(180deg, var(--card-blue-top), var(--card-blue-bottom));
  }
  .brand-band {
    position: absolute;
    left: 0; right: 0;
    top: 70px;
    height: 104px;
    background: var(--band);
    display: flex;
    flex-direction: column;
    align-items: center;
    justify-content: center;
    gap: 8px;
  }
  .brand-name {
    font-family: "Raleway", Arial, sans-serif;
    font-weight: 500;
    font-size: 26px;
    color: var(--ink-blue);
    display: flex;
    align-items: center;
    gap: 10px;
  }
  .brand-dot {
    width: 14px; height: 14px;
    border-radius: 50%;
    background: var(--ink-blue);
  }
  .tagline {
    font-family: "Oswald", Arial, sans-serif;
    font-weight: 600;
    font-size: 12.5px;
    line-height: 1.15;
    text-transform: uppercase;
    text-align: center;
    color: var(--deep-blue);
    letter-spacing: 0.2px;
  }
  .identity {
    position: absolute;
    left: 150px;
    top: 186px;
  }
  .person-name {
    font-size: 34px;
    font-weight: 400;
    color: var(--ink-blue);
    letter-spacing: 1px;
    line-height: 1;
    text-transform: uppercase;
  }
  .person-role {
    font-size: 18px;
    color: var(--title-white);
    margin-top: 2px;
    margin-left: 14px;
  }
  .contacts {
    list-style: none;
    position: absolute;
    left: 126px;
    top: 256px;
    display: flex;
    flex-direction: column;
    gap: 4px;
  }
  .contact {
    display: flex;
    align-items: center;
    gap: 12px;
    font-size: 17px;
    color: #1d2a3a;
  }
  .contact-icon {
    width: 20px; height: 20px;
    border-radius: 50%;
    background: var(--paper);
    display: flex;
    align-items: center;
    justify-content: center;
  }
  .card-back {
    background: var(--paper);
    padding: 58px 40px;
  }
  .braille {
    font-family: "Segoe UI Symbol", "DejaVu Sans", sans-serif;
    font-size: 22px;
    line-height: 1.5;
    color: var(--dots);
    letter-spacing: 3px;
  }
</style>
</head>
<body>
  <section class="card card-front" aria-label="Business card front">
    <div class="brand-band">
      <div class="brand-name"><span class="brand-dot"></span>Harlow Consulting</div>
      <p class="tagline">International development consultant connecting<br>international development with community</p>
    </div>
    <div class="identity">
      <h1 class="person-name">Mirela Harlow</h1>
      <p class="person-role">Lead Consultant</p>
    </div>
    <ul class="contacts">
      <li class="contact">
        <span class="contact-icon">
          <svg width="12" height="12" viewBox="0 0 24 24" aria-hidden="true"><path fill="#7599cb" d="M6.6 10.8a15 15 0 0 0 6.6 6.6l2.2-2.2a1 1 0 0 1 1-.25 11.4 11.4 0 0 0 3.6.57 1 1 0 0 1 1 1V20a1 1 0 0 1-1 1A17 17 0 0 1 3 4a1 1 0 0 1 1-1h3.5a1 1 0 0 1 1 1c0 1.25.2 2.45.57 3.6a1 1 0 0 1-.25 1z"/></svg>
        </span>
        +61 412 558127
      </li>
      <li class="contact">
        <span class="contact-icon">
          <svg width="12" height="12" viewBox="0 0 24 24" aria-hidden="true"><rect x="2" y="5" width="20" height="14" rx="2" fill="#7599cb"/><path d="M3 6l9 7 9-7" fill="none" stroke="#fff" stroke-width="2"/></svg>
        </span>
        mharlow.consulting@quillmail.net
      </li>
    </ul>
  </section>

  <section class="card card-back" aria-label="Business card back in braille">
    <p class="braille">⠍⠊⠗⠑⠇⠁ ⠓⠁⠗⠇⠕⠺<br>⠇⠑⠁⠙ ⠉⠕⠝⠎⠥⠇⠞⠁⠝⠞<br>⠏⠓⠕⠝⠑ ⠼⠙⠁⠃ ⠼⠑⠑⠓⠁⠃⠛<br>⠑⠍⠁⠊⠇ ⠍⠓⠁⠗⠇⠕⠺</p>
  </section>
</body>
</html>
```